Business Card Design

Psychotherapy and Therapeutic Counselling

As well as Life Coaching.

Industry/Entity Type

Business

Contact Information for Business Card

Focus
Life Coaching Services
Confidential and Compassionate
KB FdSc Qualified Practitioner

Tel 07982514630

```html
<!DOCTYPE html>
<html lang="en">
<head>
<meta charset="utf-8">
<title>Psychotherapy, Therapeutic Counselling and Life Coaching Business Card</title>
<link rel="stylesheet" href="https://fonts.googleapis.com/css2?family=Kaushan+Script&family=Arimo:wght@400&display=swap">
<style>
  :root {
    --page-bg: #ffffff;
    --card-pink: #fcd9fc;
    --bulb-tint: #f8c6f6;
    --plum: #6b0f8c;
    --violet: #5a2fd3;
    --card-white: #ffffff;
  }
  html, body {
    margin: 0;
    padding: 0;
    width: 1200px;
    height: 1000px;
    overflow: hidden;
    background: var(--page-bg);
  }
  .canvas {
    position: relative;
    width: 1200px;
    height: 1000px;
  }
  .business-card {
    position: absolute;
    left: 352px;
    top: 322px;
    width: 495px;
    height: 355px;
    background: var(--card-pink);
    overflow: hidden;
  }
  .bulb-decoration {
    position: absolute;
    left: 325px;
    top: 50px;
    width: 165px;
    height: 270px;
    border-radius: 50% 50% 30% 30% / 40% 40% 20% 20%;
    background: radial-gradient(ellipse at 50% 40%, var(--bulb-tint) 0%, rgba(248,198,246,0.5) 60%, rgba(252,217,252,0) 100%);
  }
  .swoosh {
    position: absolute;
    left: 0;
    top: 200px;
    width: 495px;
    height: 120px;
  }
  .service-heading {
    position: absolute;
    margin: 0;
    font-family: "Kaushan Script", cursive;
    font-weight: 400;
    font-size: 31px;
    line-height: 1;
    white-space: nowrap;
  }
  .service-heading--psychotherapy { left: 95px; top: 14px; color: var(--plum); }
  .service-heading--counselling { left: 38px; top: 56px; color: var(--violet); }
  .service-heading--coaching { left: 92px; top: 97px; color: var(--plum); }
  .service-heading--services { left: 114px; top: 138px; color: var(--violet); }
  .card-detail {
    position: absolute;
    margin: 0;
    font-family: "Arimo", Arial, sans-serif;
    font-size: 20px;
    color: var(--card-white);
    letter-spacing: -0.3px;
    white-space: nowrap;
  }
  .card-detail--promise { left: 37px; top: 186px; }
  .card-detail--qualification { left: 37px; top: 229px; }
  .card-detail--phone { left: 42px; top: 297px; }
</style>
</head>
<body>
<div class="canvas">
  <div class="business-card">
    <div class="bulb-decoration" role="img" aria-label="Faint light bulb illustration"></div>
    <svg class="swoosh" viewBox="0 0 495 120" aria-hidden="true">
      <path d="M0 105 C 90 70, 200 60, 330 40 C 250 70, 120 85, 0 112 Z" fill="#ffffff" fill-opacity="0.35"/>
    </svg>
    <h1 class="service-heading service-heading--psychotherapy">Psychoterapy</h1>
    <h2 class="service-heading service-heading--counselling">Therapeutic&nbsp; Counselling</h2>
    <h2 class="service-heading service-heading--coaching">Life Coaching</h2>
    <h2 class="service-heading service-heading--services">Services</h2>
    <p class="card-detail card-detail--promise">Confidential and Compassionate</p>
    <p class="card-detail card-detail--qualification">KB FdSc Qualified Practitioner</p>
    <p class="card-detail card-detail--phone">Tel: 07982514630</p>
  </div>
</div>
</body>
</html>
```